5 post cards for B2B Advertising

We are an electrical lighting contractor advertising our Lighting and Electrical services to property management companies, car dealer ships, hotels, schools, malls, and shopping centers.

RED / White / Blue themed American flag.

Post Cards

1. Electrical Services
2. Lighting Services and conversions to LED
3. Sign Repairs and conversions to LED
4. Nighttime Lighting Inspections (report lights and signs out)
5. Lighting is Safety

```html
<!DOCTYPE html>
<html lang="en">
<head>
<meta charset="utf-8">
<title>Brightline Service – Postcard Series</title>
<link rel="stylesheet" href="https://fonts.googleapis.com/css2?family=Exo+2:wght@700;800&family=Open+Sans:wght@400;600;700&display=swap">
<style>
:root{
  --backdrop:#b4b4b4;
  --blue:#2b3590;
  --red:#ed1c24;
  --white:#ffffff;
  --guide:#3fbf6f;
  --head:"Exo 2", sans-serif;
  --body:"Open Sans", sans-serif;
}
*{box-sizing:border-box}
html,body{margin:0;width:1171px;height:1200px;overflow:hidden;background:var(--backdrop)}
.sheet{position:relative;width:1171px;height:1200px}
.card{position:absolute;width:445px;height:288px;background:var(--white);overflow:hidden;outline:0.6px solid var(--red)}
.card .art{position:absolute;inset:0;width:445px;height:288px}
.card .guides{position:absolute;inset:0;pointer-events:none}
.pos-l{left:120px}.pos-r{left:600px}
.row-1{top:134px}.row-2{top:458px}.row-3{top:782px}

.brand{position:absolute;text-align:center;color:var(--red);font-family:var(--head);font-weight:800;line-height:.98;letter-spacing:.5px}
.brand .brand-line{display:block;font-size:21px}
.brand .brand-sub{display:block;font-size:8.5px;letter-spacing:.6px;margin-top:2px}

.headline{position:absolute;font-family:var(--head);font-weight:800;font-size:15.5px;line-height:1.17;color:var(--blue);letter-spacing:.3px;margin:0}
.headline .hot{color:var(--red)}
.copy{position:absolute;font-family:var(--body);font-size:7.3px;line-height:9.6px;color:var(--blue);margin:0}
.copy b{font-weight:700}
.copy.center{text-align:center}

.phone{position:absolute;display:flex;align-items:center;gap:7px;font-family:var(--body);font-weight:600;font-size:22px;color:var(--white);letter-spacing:.2px}
.phone svg{width:20px;height:20px;flex:none}
.web{position:absolute;font-family:var(--body);font-size:8.6px;color:var(--red);text-align:center}
.web.blue{color:var(--blue)}

.mail-panel-title{position:absolute;font-family:var(--body);font-weight:700;font-size:8.6px;color:var(--white);letter-spacing:.2px}
.return-address{position:absolute;font-family:var(--body);font-weight:700;font-size:7.6px;line-height:9.4px;color:var(--white)}
.contact-row{position:absolute;display:flex;align-items:center;gap:9px;font-family:var(--body);font-size:7.6px;color:var(--white)}
.contact-row svg{width:9px;height:9px;flex:none}
.callout{position:absolute;font-family:var(--head);font-weight:800;font-size:16px;color:var(--blue);text-align:center;letter-spacing:.3px}
</style>
</head>
<body>
<svg width="0" height="0" style="position:absolute">
  <defs>
    <symbol id="ico-phone" viewBox="0 0 24 24">
      <circle cx="12" cy="12" r="10.3" fill="none" stroke="#fff" stroke-width="1.8"/>
      <path d="M8.3 6.6l1.9-.4 1.2 2.9-1.3 1c.6 1.4 1.6 2.5 3 3.2l1-1.3 2.9 1.2-.4 1.9c-.2.7-.8 1.1-1.5 1.1-4.2-.4-7.7-3.8-8-8 0-.8.4-1.4 1.2-1.6z" fill="#fff"/>
    </symbol>
    <linearGradient id="g-panel" x1="0" y1="0" x2="1" y2="1"><stop offset="0" stop-color="#d9d4cc"/><stop offset=".5" stop-color="#a7985f"/><stop offset="1" stop-color="#3a3b3f"/></linearGradient>
    <linearGradient id="g-truck" x1="0" y1="0" x2="0" y2="1"><stop offset="0" stop-color="#5f7a52"/><stop offset=".5" stop-color="#d7dadd"/><stop offset="1" stop-color="#6c6a66"/></linearGradient>
    <linearGradient id="g-arena" x1="0" y1="0" x2="0" y2="1"><stop offset="0" stop-color="#8d9592"/><stop offset=".6" stop-color="#c7cdcc"/><stop offset="1" stop-color="#4e8d3e"/></linearGradient>
    <linearGradient id="g-sky" x1="0" y1="0" x2="0" y2="1"><stop offset="0" stop-color="#3f72b8"/><stop offset=".7" stop-color="#9dbbd6"/><stop offset="1" stop-color="#4d6a4a"/></linearGradient>
    <linearGradient id="g-facade" x1="0" y1="0" x2="0" y2="1"><stop offset="0" stop-color="#a7c0d9"/><stop offset=".45" stop-color="#d8c9a6"/><stop offset="1" stop-color="#7d4a3a"/></linearGradient>
    <linearGradient id="g-dusk" x1="0" y1="0" x2="0" y2="1"><stop offset="0" stop-color="#6e7584"/><stop offset=".6" stop-color="#b8b9bc"/><stop offset="1" stop-color="#4b4d50"/></linearGradient>
    <linearGradient id="g-store" x1="0" y1="0" x2="0" y2="1"><stop offset="0" stop-color="#2c3a7a"/><stop offset=".5" stop-color="#c9c7cf"/><stop offset="1" stop-color="#2a2b30"/></linearGradient>
    <linearGradient id="g-night" x1="0" y1="0" x2="1" y2="1"><stop offset="0" stop-color="#1c1a1a"/><stop offset=".6" stop-color="#4a3d2c"/><stop offset="1" stop-color="#d4d6da"/></linearGradient>
    <linearGradient id="g-field" x1="0" y1="0" x2="0" y2="1"><stop offset="0" stop-color="#121418"/><stop offset=".65" stop-color="#3a3a38"/><stop offset="1" stop-color="#a89677"/></linearGradient>
    <linearGradient id="g-lift" x1="0" y1="0" x2="0" y2="1"><stop offset="0" stop-color="#2f5fae"/><stop offset=".55" stop-color="#6a7f9b"/><stop offset="1" stop-color="#2d3326"/></linearGradient>
    <linearGradient id="g-van" x1="0" y1="0" x2="1" y2="0"><stop offset="0" stop-color="#e9ecef"/><stop offset=".7" stop-color="#f8f8f8"/><stop offset="1" stop-color="#b9bcc2"/></linearGradient>
  </defs>
</svg>

<main class="sheet">

  <!-- Card 1: Electrical Services -->
  <section class="card pos-l row-1">
    <svg class="art" viewBox="0 0 445 288">
      <polygon role="img" aria-label="Technician in hard hat and safety vest testing wiring at an electrical panel" points="0,0 181,0 221,144 0,144" fill="url(#g-panel)"/>
      <polygon points="188,0 195,0 235,144 228,144" fill="var(--blue)"/>
      <polygon role="img" aria-label="Company service truck with bucket lift and technician at the toolbox" points="221,144 445,144 445,288 276,288" fill="url(#g-truck)"/>
      <polygon points="205,144 214,144 269,288 260,288" fill="var(--red)"/>
      <polygon points="0,232 234,232 248,268 0,268" fill="var(--blue)"/>
    </svg>
    <div class="brand" style="left:238px;top:19px;width:190px">
      <span class="brand-line">BRIGHTLINE</span><span class="brand-line">SERVICE</span><span class="brand-sub">INCORPORATED</span>
    </div>
    <h2 class="headline" style="left:238px;top:93px;width:190px;text-align:center">ELECTRICAL<br><span class="hot">SERVICES</span></h2>
    <p class="copy" style="left:17px;top:152px;width:196px"><b>Power Up</b> Your Business with our <b>Electrical Services!</b> From <b>wiring upgrades</b> and <b>energy-efficient lighting</b> installations to <b>electrical maintenance</b> and <b>emergency repairs</b>, we are your trusted partner for all commercial electrical needs. Let our <b>expert team</b> keep your business running smoothly and safely. Contact us today for <b>reliable service</b> you can count on!</p>
    <div class="phone" style="left:28px;top:236px"><svg><use href="#ico-phone"/></svg>877-555-0148</div>
    <div class="web" style="left:0;top:270px;width:220px">www.brightlineservice.com</div>
    <svg class="guides" viewBox="0 0 445 288"><rect x="4.5" y="4.5" width="436" height="279" fill="none" stroke="var(--guide)" stroke-width=".6" stroke-dasharray="3 2"/></svg>
  </section>

  <!-- Card 2: Lighting Services and Conversions to LED -->
  <section class="card pos-r row-1">
    <svg class="art" viewBox="0 0 445 288">
      <polygon role="img" aria-label="Indoor sports facility lit by overhead LED fixtures above green turf" points="224,0 445,0 445,144 274,144" fill="url(#g-arena)"/>
      <polygon points="249,151 445,151 445,156 251,156" fill="var(--red)"/>
      <polygon role="img" aria-label="Technician in harness servicing stadium floodlights against blue sky" points="0,144 184,144 224,288 0,288" fill="url(#g-sky)"/>
      <polygon points="188,176 195,176 239,288 232,288" fill="var(--blue)"/>
      <polygon points="214,231 445,231 445,267 228,267" fill="var(--red)"/>
    </svg>
    <div class="brand" style="left:29px;top:19px;width:190px">
      <span class="brand-line">BRIGHTLINE</span><span class="brand-line">SERVICE</span><span class="brand-sub">INCORPORATED</span>
    </div>
    <h2 class="headline" style="left:4px;top:89px;width:240px;text-align:center"><span class="hot">LIGHTING SERVICES</span> AND<br>CONVERSIONS TO LED</h2>
    <p class="copy" style="left:229px;top:167px;width:184px"><b>Illuminate Your World</b> with Brightline Service Inc! We specialize in <b>outdoor lighting solutions</b>, from <b>LED security lights</b> to <b>dazzling signs</b>. Trust us to brighten up your space with top-notch expertise and quality service.</p>
    <div class="phone" style="left:248px;top:235px"><svg><use href="#ico-phone"/></svg>877-555-0148</div>
    <div class="web blue" style="left:232px;top:270px;width:200px">www.brightlineservice.com</div>
    <svg class="guides" viewBox="0 0 445 288"><rect x="4.5" y="4.5" width="436" height="279" fill="none" stroke="var(--guide)" stroke-width=".6" stroke-dasharray="3 2"/></svg>
  </section>

  <!-- Card 3: Sign Repairs and Conversions to LED -->
  <section class="card pos-l row-2">
    <svg class="art" viewBox="0 0 445 288">
      <polygon role="img" aria-label="Technician in bucket lift repairing a storefront sign on a brick restaurant" points="273,0 445,0 445,143 224,143" fill="url(#g-facade)"/>
      <polygon points="262,0 269,0 220,143 213,143" fill="var(--blue)"/>
      <polygon role="img" aria-label="Crew on lift beside a light pole with company trucks in a parking lot at dusk" points="0,143 221,143 178,288 0,288" fill="url(#g-dusk)"/>
      <polygon points="229,143 237,143 192,288 184,288" fill="var(--red)"/>
      <polygon points="214,228 445,228 445,264 203,264" fill="var(--red)"/>
    </svg>
    <h2 class="headline" style="left:21px;top:21px;width:200px">SIGN REPAIRS <span class="hot">AND<br>CONVERSIONS TO LED</span></h2>
    <p class="copy" style="left:21px;top:67px;width:172px"><b>Light Up the Night</b> with Brightline Service Inc! Whether you need reliable <b>LED security lights</b> or <b>eye-catching signage</b>, our skilled team has got you covered. From commercial properties to pro stadiums, we deliver exceptional <b>outdoor lighting solutions</b> that shine bright.</p>
    <div class="brand" style="left:232px;top:159px;width:190px">
      <span class="brand-line">BRIGHTLINE</span><span class="brand-line">SERVICE</span><span class="brand-sub">INCORPORATED</span>
    </div>
    <div class="phone" style="left:242px;top:232px"><svg><use href="#ico-phone"/></svg>877-555-0148</div>
    <div class="web" style="left:222px;top:270px;width:200px">www.brightlineservice.com</div>
    <svg class="guides" viewBox="0 0 445 288"><rect x="4.5" y="4.5" width="436" height="279" fill="none" stroke="var(--guide)" stroke-width=".6" stroke-dasharray="3 2"/></svg>
  </section>

  <!-- Card 4: Nighttime Lighting Inspections -->
  <section class="card pos-r row-2">
    <svg class="art" viewBox="0 0 445 288">
      <polygon role="img" aria-label="Large retail storefront illuminated at night" points="0,0 172,0 221,143 0,143" fill="url(#g-store)"/>
      <polygon points="180,0 188,0 236,143 228,143" fill="var(--red)"/>
      <polygon role="img" aria-label="Inspector with tablet checking parking lot lights beside a company van at night" points="222,143 445,143 445,288 262,288" fill="url(#g-night)"/>
      <polygon points="205,143 212,143 253,288 246,288" fill="var(--blue)"/>
      <polygon points="0,228 224,228 237,264 0,264" fill="var(--red)"/>
    </svg>
    <h2 class="headline" style="left:234px;top:14px;width:200px;text-align:center"><span class="hot">NIGHTTIME LIGHTING</span><br>INSPECTIONS</h2>
    <p class="copy center" style="left:236px;top:50px;width:196px;font-size:6.1px;line-height:9.3px">Brightline Service Inc is here to <b>brighten your nights</b> and keep your <b>signs shining!</b> Introducing our <b>Night Time Lighting and Sign Inspection Service</b> - a comprehensive evaluation of your property's <b>outdoor lighting and signage</b>, all for free. Our expert team will meticulously inspect every detail, using a map of your property to ensure thorough coverage. Trust us to <b>enhance visibility, security, and aesthetics</b> with our professional services. Schedule your complimentary inspection today and light up the night with confidence!</p>
    <div class="brand" style="left:25px;top:159px;width:190px">
      <span class="brand-line">BRIGHTLINE</span><span class="brand-line">SERVICE</span><span class="brand-sub">INCORPORATED</span>
    </div>
    <div class="phone" style="left:33px;top:232px"><svg><use href="#ico-phone"/></svg>877-555-0148</div>
    <div class="web" style="left:14px;top:270px;width:200px">www.brightlineservice.com</div>
    <svg class="guides" viewBox="0 0 445 288"><rect x="4.5" y="4.5" width="436" height="279" fill="none" stroke="var(--guide)" stroke-width=".6" stroke-dasharray="3 2"/></svg>
  </section>

  <!-- Card 5: Lighting is Safety -->
  <section class="card pos-l row-3">
    <svg class="art" viewBox="0 0 445 288">
      <polygon role="img" aria-label="Athletic field lit by tall floodlight poles at night" points="273,0 445,0 445,143 224,143" fill="url(#g-field)"/>
      <polygon points="262,0 269,0 220,143 213,143" fill="var(--blue)"/>
      <polygon role="img" aria-label="Red aerial lift truck raising crew to a bright stadium light at dusk" points="0,143 221,143 178,288 0,288" fill="url(#g-lift)"/>
      <polygon points="229,143 237,143 192,288 184,288" fill="var(--red)"/>
      <polygon points="214,228 445,228 445,264 203,264" fill="var(--blue)"/>
    </svg>
    <h2 class="headline" style="left:21px;top:28px;width:200px"><span class="hot">LIGHTING</span> IS SAFETY</h2>
    <p class="copy" style="left:21px;top:68px;width:180px"><b>Brighten Every Moment</b> with Brightline Service Inc! Specializing in <b>outdoor lighting</b>. Experience the difference of working with a <b>premier electrical contractor</b> who delivers excellence every time.</p>
    <div class="brand" style="left:240px;top:160px;width:190px">
      <span class="brand-line">BRIGHTLINE</span><span class="brand-line">SERVICE</span><span class="brand-sub">INCORPORATED</span>
    </div>
    <div class="phone" style="left:251px;top:232px"><svg><use href="#ico-phone"/></svg>877-555-0148</div>
    <div class="web" style="left:231px;top:270px;width:200px">www.brightlineservice.com</div>
    <svg class="guides" viewBox="0 0 445 288"><rect x="4.5" y="4.5" width="436" height="279" fill="none" stroke="var(--guide)" stroke-width=".6" stroke-dasharray="3 2"/></svg>
  </section>

  <!-- Card 6: Mailing side -->
  <section class="card pos-r row-3">
    <svg class="art" viewBox="0 0 445 288">
      <rect x="249" y="0" width="196" height="288" fill="var(--blue)"/>
      <rect x="237" y="0" width="6" height="146" fill="var(--red)"/>
      <rect x="249" y="82" width="196" height="30" fill="var(--red)"/>
      <rect x="383" y="27" width="49" height="48" fill="var(--white)"/>
      <g stroke="var(--blue)" stroke-width=".8">
        <line x1="17" y1="99" x2="220" y2="99"/>
        <line x1="17" y1="117" x2="220" y2="117"/>
        <line x1="17" y1="135" x2="220" y2="135"/>
        <line x1="17" y1="153" x2="220" y2="153"/>
      </g>
      <rect x="0" y="237" width="250" height="37" fill="var(--red)"/>
      <path role="img" aria-label="White company service van with roof racks" d="M236 160 Q240 132 268 126 L300 118 L445 108 L445 282 L300 282 Q250 280 232 250 Z" fill="url(#g-van)"/>
    </svg>
    <div class="brand" style="left:30px;top:13px;width:190px">
      <span class="brand-line" style="font-size:17px">BRIGHTLINE</span><span class="brand-line" style="font-size:17px">SERVICE</span><span class="brand-sub" style="font-size:7px">INCORPORATED</span>
    </div>
    <div class="mail-panel-title" style="left:261px;top:12px">CONTACT INFO / RETURN</div>
    <div class="return-address" style="left:261px;top:45px">Brightline Service Inc<br>412 Harbor Lane Norfolk<br>VA 23510</div>
    <div class="contact-row" style="left:261px;top:86px">
      <svg viewBox="0 0 10 10"><rect x=".6" y="1.8" width="8.8" height="6.4" fill="none" stroke="#fff" stroke-width="1"/><path d="M.8 2.2L5 5.6 9.2 2.2" fill="none" stroke="#fff" stroke-width="1"/></svg>
      www.brightlineservice.com
    </div>
    <div class="contact-row" style="left:261px;top:97px">
      <svg viewBox="0 0 10 10"><circle cx="5" cy="5" r="4.3" fill="none" stroke="#fff" stroke-width=".9"/><ellipse cx="5" cy="5" rx="1.9" ry="4.3" fill="none" stroke="#fff" stroke-width=".8"/><line x1=".7" y1="5" x2="9.3" y2="5" stroke="#fff" stroke-width=".8"/></svg>
      office@brightlineservice.com
    </div>
    <div class="callout" style="left:20px;top:215px;width:210px">CALL US TODAY!</div>
    <div class="phone" style="left:38px;top:243px"><svg><use href="#ico-phone"/></svg>877-555-0148</div>
    <svg class="guides" viewBox="0 0 445 288"><rect x="4.5" y="4.5" width="436" height="279" fill="none" stroke="var(--guide)" stroke-width=".6" stroke-dasharray="3 2"/></svg>
  </section>

</main>
</body>
</html>
```